Business Card Design for Loft Pictures

Hi we need a business card designed for a new aerial photography business we have started, we use UAV Drones to take photos for corporate, events, real estate, local government etc , the business name is Loft Pictures Australia, we have a facebook page that might help you come up with some designs - https://www.facebook.com/loftpicturesaustralia

We need to have and editable AI file so that we can use different names and contact details. details for one of the cards as follow:

Ned Harrow
phone: 03 5521 4736
Mobile: 0431 957 284
email: ned@loftpicturez.example
web: www.loftpictures.example

have now changed: Designer Payment:Committed

Target Market(s)

We are a Aerial Photography business using Drones and UAV

Industry/Entity Type

Business

Logo Text

Loft Pictures Australia

Requirements
Must have
• Colors to match logo and be part of Loft Pictures Brand

```html
<!DOCTYPE html>
<html lang="en">
<head>
<meta charset="utf-8">
<title>Loft Pictures Australia – Business Card</title>
<link rel="stylesheet" href="https://fonts.googleapis.com/css2?family=Open+Sans:wght@400;700&display=swap">
<style>
  :root {
    --backdrop: #e6e6e6;
    --card-white: #ffffff;
    --card-dark: #2b2b2b;
    --sky-blue: #29a9e1;
    --sky-light: #bfe6f7;
    --swoosh-black: #1f1f1f;
    --swoosh-grey: #9a9a9a;
    --ink: #3a3a3a;
    --ink-soft: #4a4a4a;
    --white: #ffffff;
    --divider: #b5b5b5;
  }
  * { margin: 0; padding: 0; box-sizing: border-box; }
  html, body {
    width: 1200px;
    height: 1102px;
    overflow: hidden;
    background: var(--backdrop);
    font-family: "Open Sans", Arial, sans-serif;
  }
  .canvas { position: relative; width: 1200px; height: 1102px; }

  .card {
    position: absolute;
    border-radius: 30px;
    overflow: hidden;
    box-shadow: 0 4px 14px rgba(0,0,0,0.18);
  }

  /* Front */
  .card-front {
    left: 43px; top: 28px;
    width: 880px; height: 503px;
    background: var(--card-white);
  }
  .front-swoosh { position: absolute; inset: 0; }
  .holder-name {
    position: absolute;
    right: 40px; top: 50px;
    color: var(--white);
    font-weight: 700;
    font-size: 25px;
    letter-spacing: 0.02em;
  }
  .brand-front {
    position: absolute;
    left: 69px; top: 140px;
    color: var(--ink);
    font-weight: 700;
    line-height: 1;
  }
  .brand-front .brand-line-1 { display: block; font-size: 86px; letter-spacing: 0.04em; }
  .brand-front .brand-line-2 { display: block; font-size: 62px; letter-spacing: 0.02em; margin-top: 6px; }
  .brand-front .brand-line-3 { display: block; font-size: 26px; letter-spacing: 0.42em; margin-top: 16px; padding-left: 92px; }

  .contact {
    position: absolute;
    top: 420px;
    list-style: none;
    font-size: 20px;
    color: var(--ink-soft);
  }
  .contact li { display: flex; align-items: center; height: 36px; }
  .contact svg { width: 20px; height: 20px; margin-right: 10px; flex: none; }
  .contact-phones { left: 72px; }
  .contact-online { left: 288px; }
  .contact-divider {
    position: absolute;
    left: 265px; top: 422px;
    width: 1px; height: 70px;
    background: var(--divider);
  }

  /* Back */
  .card-back {
    left: 277px; top: 557px;
    width: 877px; height: 504px;
    background: var(--card-dark);
    color: var(--white);
    text-align: center;
  }
  .brand-back {
    position: absolute;
    left: 0; right: 0; top: 92px;
    font-weight: 700;
    line-height: 1;
  }
  .brand-back .brand-line-1 { display: block; font-size: 112px; letter-spacing: 0.05em; }
  .brand-back .brand-line-2 { display: block; font-size: 84px; letter-spacing: 0.02em; margin-top: 14px; }
  .brand-back .brand-line-3 { display: block; font-size: 34px; letter-spacing: 0.42em; margin-top: 34px; padding-left: 0.42em; }
  .back-url {
    position: absolute;
    left: 0; right: 0; top: 428px;
    font-size: 25px;
    letter-spacing: 0.16em;
  }
</style>
</head>
<body>
<main class="canvas">

  <section class="card card-front" aria-label="Business card front">
    <svg class="front-swoosh" viewBox="0 0 880 503" preserveAspectRatio="none" aria-hidden="true">
      <defs>
        <linearGradient id="skyFade" x1="0" y1="0" x2="1" y2="0">
          <stop offset="0" stop-color="var(--sky-light)"/>
          <stop offset="0.35" stop-color="var(--sky-blue)"/>
          <stop offset="1" stop-color="var(--sky-blue)"/>
        </linearGradient>
      </defs>
      <path d="M0,0 H880 V235 C640,90 330,45 0,110 Z" fill="url(#skyFade)"/>
      <path d="M0,150 C300,55 640,80 880,228 L880,275 C640,130 320,90 0,160 Z" fill="var(--swoosh-black)"/>
      <path d="M0,128 C180,88 380,72 600,80" fill="none" stroke="var(--swoosh-grey)" stroke-width="7"/>
    </svg>

    <p class="holder-name">NED HARROW</p>

    <h1 class="brand-front">
      <span class="brand-line-1">LOFT</span>
      <span class="brand-line-2">PICTURES</span>
      <span class="brand-line-3">AUSTRALIA</span>
    </h1>

    <ul class="contact contact-phones">
      <li>
        <svg viewBox="0 0 20 20" aria-hidden="true"><circle cx="10" cy="10" r="9" fill="none" stroke="var(--sky-blue)" stroke-width="1.6"/><path d="M7 5.5 L8.6 8 L7.6 9 C8.3 10.6 9.4 11.7 11 12.4 L12 11.4 L14.5 13 L13.5 14.8 C9.5 14.5 5.5 10.5 5.2 6.5 Z" fill="var(--sky-blue)"/></svg>
        03 5521 4736
      </li>
      <li>
        <svg viewBox="0 0 20 20" aria-hidden="true"><rect x="5.5" y="1.5" width="9" height="17" rx="1.6" fill="var(--sky-blue)"/><rect x="7" y="3.5" width="6" height="9" fill="var(--white)"/><circle cx="10" cy="15.6" r="1.1" fill="var(--white)"/></svg>
        0431 957 284
      </li>
    </ul>

    <div class="contact-divider" aria-hidden="true"></div>

    <ul class="contact contact-online">
      <li>
        <svg viewBox="0 0 20 20" aria-hidden="true"><rect x="2" y="5" width="16" height="11" rx="1.5" fill="var(--sky-blue)"/><path d="M2.5 6 L10 11.5 L17.5 6" fill="none" stroke="var(--white)" stroke-width="1.5"/></svg>
        name@loftpicturez.example
      </li>
      <li>
        <svg viewBox="0 0 20 20" aria-hidden="true"><circle cx="10" cy="10" r="8" fill="var(--sky-blue)"/><g fill="none" stroke="var(--white)" stroke-width="1.1"><ellipse cx="10" cy="10" rx="3.4" ry="8"/><path d="M2 10 H18 M3.5 6 H16.5 M3.5 14 H16.5"/></g></svg>
        www.loftpictures.example
      </li>
    </ul>
  </section>

  <section class="card card-back" aria-label="Business card back">
    <h2 class="brand-back">
      <span class="brand-line-1">LOFT</span>
      <span class="brand-line-2">PICTURES</span>
      <span class="brand-line-3">AUSTRALIA</span>
    </h2>
    <p class="back-url">www.loftpictures.example</p>
  </section>

</main>
</body>
</html>
```